Business cards and stationary for Mortgage Company
Brightwell Lending Partners Inc.
Professional
Peter K Ostrand
Licensed Mortgage Originator
47 Alder Brook Lane
Newtown, Pa 18977
1-855-314-HOME (4663)
peterkostrand@brightwelllendingpartners.example
www.brightwelllendingpartners.example
NMLS# 417205 and NMLS #418362
Looking for stationary and business cards to use logo with black letters on white background, and examples using white letters on black ground . Red graphic is the same on either choice.
Just the logo in either black on white, or white on black background.

```html
<!DOCTYPE html>
<html lang="en">
<head>
<meta charset="utf-8">
<title>Brightwell Lending Partners — Business Cards</title>
<link rel="stylesheet" href="https://fonts.googleapis.com/css2?family=Tinos:wght@400;700&display=swap">
<style>
  :root {
    --backdrop: #e4e6e8;
    --card-black: #0d0d0d;
    --card-white: #ffffff;
    --ink: #1a1a1a;
    --ink-soft: #444444;
    --brand-red: #d7261e;
    --rule-light: #9a9a9a;
    --rule-dark: #6a6a6a;
  }
  * { box-sizing: border-box; margin: 0; padding: 0; }
  html, body { width: 1200px; height: 1009px; overflow: hidden; }
  body {
    background: var(--backdrop);
    font-family: "Tinos", "Times New Roman", serif;
    display: flex;
    flex-direction: column;
    align-items: center;
    justify-content: center;
    gap: 56px;
  }
  .card {
    width: 760px;
    height: 434px;
    border-radius: 22px;
    position: relative;
    overflow: hidden;
    box-shadow: 0 10px 26px rgba(0,0,0,0.18);
  }
  .card--front { background: var(--card-black); color: #fff; }
  .card--back { background: var(--card-white); color: var(--ink); }

  .brand {
    position: absolute;
    left: 0; right: 0;
    display: flex;
    align-items: center;
    justify-content: center;
    gap: 16px;
  }
  .brand__mark {
    width: 26px; height: 26px;
    background: var(--brand-red);
  }
  .brand__name {
    font-size: 40px;
    font-weight: 400;
    letter-spacing: 0.5px;
  }
  .brand__rule {
    position: absolute;
    left: 120px; right: 120px;
    height: 1px;
  }
  .card--front .brand { top: 170px; }
  .card--front .brand__rule { top: 236px; background: var(--rule-dark); }
  .card--back .brand { top: 48px; }
  .card--back .brand__name { color: var(--ink); }
  .card--back .brand__rule { top: 114px; background: var(--rule-light); left: 70px; right: 70px; }

  .originator {
    position: absolute;
    left: 70px; width: 290px; top: 186px;
    text-align: center;
  }
  .originator__name { font-size: 22px; color: var(--ink-soft); }
  .originator__title { font-size: 18px; color: var(--brand-red); margin-top: 4px; }

  .contact {
    position: absolute;
    left: 380px; right: 40px; top: 150px;
    font-size: 15px;
    line-height: 1.6;
    color: var(--ink-soft);
  }
  .contact__licence { color: var(--brand-red); font-size: 13px; letter-spacing: 0.5px; margin-bottom: 4px; }
  .contact__row { display: flex; align-items: center; gap: 8px; white-space: nowrap; }
  .contact__icon { width: 13px; height: 13px; flex: none; }
  .contact__spacer { width: 13px; flex: none; }
</style>
</head>
<body>

  <section class="card card--front" aria-label="Card front">
    <div class="brand">
      <span class="brand__mark"></span>
      <span class="brand__name">Brightwell Lending Partners</span>
    </div>
    <div class="brand__rule"></div>
  </section>

  <section class="card card--back" aria-label="Card back">
    <div class="brand">
      <span class="brand__mark"></span>
      <span class="brand__name">Brightwell Lending Partners</span>
    </div>
    <div class="brand__rule"></div>

    <div class="originator">
      <p class="originator__name">Peter K Ostrand</p>
      <p class="originator__title">Licensed Mortgage Originator</p>
    </div>

    <div class="contact">
      <p class="contact__licence">NMLS# 417205 &nbsp; NMLS #418362</p>
      <p class="contact__row"><span class="contact__spacer"></span>47 Alder Brook Lane</p>
      <p class="contact__row"><span class="contact__spacer"></span>Maplecrest, Pa 18977</p>
      <p class="contact__row">
        <svg class="contact__icon" viewBox="0 0 16 16"><path d="M3 1h3l1.5 4-2 1.2a9 9 0 0 0 4.3 4.3L11 8.5l4 1.5v3c0 1-1 2-2 2C6.5 15 1 9.5 1 3c0-1 1-2 2-2z" fill="var(--brand-red)"/></svg>
        1-855-314-HOME (4663) (Toll Free)
      </p>
      <p class="contact__row">
        <svg class="contact__icon" viewBox="0 0 16 16"><path d="M3 1h3l1.5 4-2 1.2a9 9 0 0 0 4.3 4.3L11 8.5l4 1.5v3c0 1-1 2-2 2C6.5 15 1 9.5 1 3c0-1 1-2 2-2z" fill="var(--brand-red)"/></svg>
        215-555-0142
      </p>
      <p class="contact__row">
        <svg class="contact__icon" viewBox="0 0 16 16"><rect x="2" y="5" width="12" height="8" fill="var(--brand-red)"/><rect x="4" y="1" width="8" height="4" fill="none" stroke="var(--brand-red)" stroke-width="1.5"/></svg>
        267-555-0187
      </p>
      <p class="contact__row">
        <svg class="contact__icon" viewBox="0 0 16 16"><rect x="1" y="3" width="14" height="10" fill="var(--brand-red)"/><path d="M1 3l7 6 7-6" fill="none" stroke="#fff" stroke-width="1.3"/></svg>
        peterkostrand@brightwelllendingpartners.example
      </p>
      <p class="contact__row">
        <svg class="contact__icon" viewBox="0 0 16 16"><circle cx="8" cy="8" r="7" fill="var(--brand-red)"/></svg>
        www.brightwelllendingpartners.example
      </p>
    </div>
  </section>

</body>
</html>
```